Cosmetic injections clinic needs a fresh looking business card

We need a business card using the supplied logo and color scheme to attract future clients to our clinic. It should be modern and fresh, eye catching and not too busy. Simple and to the point is best. I would like two sided designs with the front indicating address and contact information, and the back in full color with white logo and descriptive information also provided.
Target Market(s)
Clients looking for non surgical beauty enhancements.
Contact Information for Business Card
MeloraSkin
14, 618 Birchmont Way
St. Albert, Alberta
K2P 7W3
Phone: 587-412-6630
Email: info@meloraskin.com
Requirements
Must have
- -Logo supplied with the name and address of the clinic
- -Back of card in full color with white logo with A small line of text indicating both of the following: Anti aging consultants and cosmetic injectables
- Located inside the Voyager Wellness Group

```html
<!DOCTYPE html>
<html lang="en">
<head>
<meta charset="utf-8">
<title>MeloraSkin Business Card</title>
<link href="https://fonts.googleapis.com/css2?family=Montserrat:wght@600;700&family=Open+Sans:wght@400;600&display=swap" rel="stylesheet">
<style>
  :root {
    --pink: #e0459a;
    --pink-soft: #e868ad;
    --purple: #6b42a3;
    --lavender: #ebe7f3;
    --white: #ffffff;
    --paper: #f7f7f8;
    --stage: #e9e9ec;
  }
  * { margin: 0; padding: 0; box-sizing: border-box; }
  html, body {
    width: 1200px; height: 864px; overflow: hidden;
    background: var(--stage);
  }
  .canvas {
    width: 1200px; height: 864px;
    display: flex; flex-direction: column;
    align-items: center; justify-content: center; gap: 40px;
  }
  .card {
    position: relative;
    width: 640px; height: 366px;
    border-radius: 26px;
    overflow: hidden;
    box-shadow: 0 10px 28px rgba(0,0,0,0.12);
  }
  .decor-mark {
    position: absolute; width: 330px; height: 330px; border-radius: 50%;
  }
  .brand {
    position: absolute; display: flex; align-items: center; gap: 14px;
  }
  .brand-dot { width: 44px; height: 44px; border-radius: 50%; }
  .brand-name {
    font-family: "Montserrat", sans-serif; font-weight: 700;
    font-size: 46px; letter-spacing: 0.5px;
  }

  /* Back side */
  .card-back { background: var(--pink); }
  .card-back .decor-mark { background: var(--pink-soft); right: -40px; top: -60px; }
  .card-back .brand { left: 120px; top: 140px; color: var(--white); }
  .card-back .brand-dot { background: var(--white); }
  .tagline {
    position: absolute; left: 48px; bottom: 40px;
    font-family: "Open Sans", sans-serif; font-weight: 600;
    font-size: 15px; line-height: 1.45; color: var(--white);
  }

  /* Front side */
  .card-front { background: var(--paper); }
  .card-front .decor-mark { background: var(--lavender); right: 30px; top: -40px; }
  .card-front .brand { left: 60px; top: 112px; color: var(--purple); }
  .card-front .brand-dot { background: var(--pink); }
  .rule { position: absolute; height: 1.5px; background: var(--purple); }
  .rule-address { left: 60px; width: 300px; top: 222px; }
  .rule-contact { right: 40px; width: 260px; top: 96px; }
  .address {
    position: absolute; left: 60px; top: 236px;
    font-family: "Open Sans", sans-serif; font-size: 17px; line-height: 1.45;
    color: var(--purple);
  }
  .contact {
    position: absolute; right: 40px; top: 108px; text-align: right;
    font-family: "Open Sans", sans-serif; font-size: 16px; line-height: 1.6;
    color: var(--purple);
  }
  .contact .label { color: var(--pink); }
</style>
</head>
<body>
<main class="canvas">
  <section class="card card-back">
    <div class="decor-mark" role="img" aria-label="Faint brand emblem decoration"></div>
    <div class="brand">
      <span class="brand-dot"></span>
      <span class="brand-name">MeloraSkin</span>
    </div>
    <p class="tagline">Anti Aging Consultants and Cosmetic Injectables<br>Located inside the Voyager Wellness Group</p>
  </section>

  <section class="card card-front">
    <div class="decor-mark" role="img" aria-label="Faint brand emblem decoration"></div>
    <div class="brand">
      <span class="brand-dot"></span>
      <span class="brand-name">MeloraSkin</span>
    </div>
    <div class="rule rule-address"></div>
    <p class="address">14, 618 Birchmont Way, St. Albert<br>Alberta, K2P 7W3</p>
    <div class="rule rule-contact"></div>
    <p class="contact">
      <span class="label">P:</span> 587-412-6630<br>
      <span class="label">E:</span> info@meloraskin.com
    </p>
  </section>
</main>
</body>
</html>
```